11 x 11 Flyer Design for Social Media - Reverse Mortgages

62 or older?

A Reverse Mortgage
could be
Your Road to Financial Freedom

* No Monthly Payments
* No Income Requirements
* No Credit Score Requirements
* No Loss of Ownership

Receive cash by lump sum, monthly installments or a line of credit!!

Call us today for a Free Consultation!!
(800) 471-2965

Bluegate Financial Services, Inc.
NMLS #318760
www.bluegatehome.com

```html
<!DOCTYPE html>
<html lang="en">
<head>
<meta charset="utf-8">
<title>Reverse Mortgages – Bluegate Financial Services, Inc.</title>
<link rel="stylesheet" href="https://fonts.googleapis.com/css2?family=Libre+Baskerville:wght@400;700&family=Montserrat:wght@400;600;700;800&family=League+Gothic&display=swap">
<style>
  :root{
    --brand-blue:#1662a7;
    --brand-gold:#ab9e34;
    --gold-soft:#e4dcb0;
    --paper:#ffffff;
    --photo-light:#ece3d8;
    --photo-mid:#c49a78;
    --photo-dark:#6b4330;
  }
  html,body{margin:0;padding:0;width:1200px;height:1200px;overflow:hidden;background:var(--paper);}
  .flyer{display:block;width:1200px;height:1200px;}
  .brand-name{font-family:"Libre Baskerville",serif;font-weight:400;fill:var(--brand-blue);}
  .age-prompt{font-family:"Montserrat",sans-serif;font-weight:700;fill:var(--brand-gold);}
  .headline{font-family:"Libre Baskerville",serif;font-weight:700;fill:var(--brand-blue);}
  .tagline{font-family:"Montserrat",sans-serif;font-weight:700;fill:var(--brand-gold);}
  .benefit-label{font-family:"Montserrat",sans-serif;font-weight:400;fill:var(--paper);}
  .payout-options{font-family:"Montserrat",sans-serif;font-weight:800;fill:var(--paper);}
  .cta-heading{font-family:"League Gothic",sans-serif;fill:var(--paper);letter-spacing:1px;}
  .cta-phone{font-family:"Montserrat",sans-serif;font-weight:700;fill:var(--paper);}
  .cta-web{font-family:"Montserrat",sans-serif;font-weight:400;fill:var(--paper);letter-spacing:9px;}
  .cta-license{font-family:"Montserrat",sans-serif;font-weight:700;fill:var(--paper);letter-spacing:2px;}
  .icon-ring{fill:none;stroke:var(--paper);stroke-width:3;}
  .icon-line{fill:none;stroke:var(--paper);stroke-width:4;stroke-linecap:round;stroke-linejoin:round;}
  .icon-fill{fill:var(--paper);}
</style>
</head>
<body>
<svg class="flyer" viewBox="0 0 1200 1200" xmlns="http://www.w3.org/2000/svg">
  <defs>
    <linearGradient id="photoTone" x1="0" y1="0" x2="1" y2="1">
      <stop offset="0" stop-color="var(--photo-light)"/>
      <stop offset="0.45" stop-color="var(--photo-mid)"/>
      <stop offset="1" stop-color="var(--photo-dark)"/>
    </linearGradient>
  </defs>

  <!-- Brand -->
  <g class="brand">
    <circle cx="68" cy="112" r="38" fill="var(--gold-soft)"/>
    <text class="brand-name" x="122" y="102" font-size="24">Bluegate</text>
    <text class="brand-name" x="122" y="134" font-size="19">Financial Services, Inc.</text>
  </g>

  <!-- Headline -->
  <g class="title-block">
    <text class="age-prompt" x="25" y="214" font-size="24">62 OR OLDER?</text>
    <text class="headline" x="25" y="292" font-size="57">REVERSE</text>
    <text class="headline" x="25" y="346" font-size="57">MORTGAGES</text>
    <rect x="25" y="357" width="126" height="3" fill="var(--brand-gold)"/>
    <text class="tagline" x="25" y="388" font-size="19">YOUR ROAD TO FINANCIAL FREEDOM</text>
  </g>

  <!-- Family photo area -->
  <path class="family-photo" role="img" aria-label="Photo of a smiling family of four relaxing together on a white bed"
        d="M0,424 C170,405 390,420 600,540 L760,1200 L0,1200 Z" fill="url(#photoTone)"/>

  <!-- Call to action panel (behind the benefits circle) -->
  <circle class="cta-panel" cx="1270" cy="1230" r="728" fill="var(--brand-gold)" stroke="var(--paper)" stroke-width="14"/>

  <!-- Benefits circle -->
  <circle class="benefits-panel" cx="969" cy="348" r="452" fill="var(--brand-blue)" stroke="var(--paper)" stroke-width="14"/>

  <g class="benefit">
    <circle class="icon-ring" cx="795" cy="154" r="59"/>
    <rect class="icon-line" x="776" y="130" width="32" height="54" rx="5"/>
    <path class="icon-line" d="M766,130 a14,14 0 0 1 0,-12 M759,134 a24,24 0 0 1 0,-22"/>
    <rect class="icon-fill" x="788" y="158" width="30" height="20" rx="3"/>
    <text class="benefit-label" x="795" y="244" font-size="25" text-anchor="middle">No Monthly</text>
    <text class="benefit-label" x="795" y="272" font-size="25" text-anchor="middle">Payments</text>
  </g>

  <g class="benefit">
    <circle class="icon-ring" cx="1014" cy="154" r="59"/>
    <path class="icon-line" d="M985,160 v22 M985,166 h22 l20,-10"/>
    <rect class="icon-fill" x="994" y="142" width="22" height="5" rx="2"/>
    <rect class="icon-fill" x="994" y="134" width="22" height="5" rx="2"/>
    <rect class="icon-fill" x="994" y="126" width="22" height="5" rx="2"/>
    <circle class="icon-line" cx="1030" cy="132" r="8"/>
    <text class="benefit-label" x="1014" y="244" font-size="25" text-anchor="middle">No Income</text>
    <text class="benefit-label" x="1014" y="272" font-size="25" text-anchor="middle">Requirements</text>
  </g>

  <g class="benefit">
    <circle class="icon-ring" cx="795" cy="356" r="59"/>
    <path d="M758,366 a37,37 0 0 1 74,0" fill="none" stroke="var(--paper)" stroke-width="9" stroke-linecap="round"/>
    <path class="icon-line" d="M795,374 L825,340"/>
    <text class="benefit-label" x="795" y="451" font-size="25" text-anchor="middle">No Credit Score</text>
    <text class="benefit-label" x="795" y="479" font-size="25" text-anchor="middle">Requirements</text>
  </g>

  <g class="benefit">
    <circle class="icon-ring" cx="1014" cy="356" r="59"/>
    <circle class="icon-line" cx="1004" cy="334" r="7"/>
    <path class="icon-line" d="M1011,334 h37 M1040,334 v7 M1047,334 v7"/>
    <path class="icon-fill" d="M978,372 c10,-12 26,-14 40,-8 l20,-6 c6,-2 10,6 4,9 l-30,18 c-10,5 -26,4 -34,-2 z"/>
    <text class="benefit-label" x="1014" y="451" font-size="25" text-anchor="middle">No Loss of</text>
    <text class="benefit-label" x="1014" y="479" font-size="25" text-anchor="middle">Ownership</text>
  </g>

  <g class="payout">
    <text class="payout-options" x="897" y="562" font-size="30" text-anchor="middle">RECEIVE CASH BY</text>
    <text class="payout-options" x="897" y="598" font-size="30" text-anchor="middle">LUMP SUM, MONTHLY</text>
    <text class="payout-options" x="897" y="634" font-size="30" text-anchor="middle">INSTALLMENTS OR A</text>
    <text class="payout-options" x="897" y="669" font-size="30" text-anchor="middle">LINE OF CREDIT!!</text>
  </g>

  <g class="cta">
    <text class="cta-heading" x="671" y="941" font-size="74">CALL US TODAY FOR A</text>
    <text class="cta-heading" x="671" y="1008" font-size="74">FREE CONSULTATION!!</text>
    <text class="cta-phone" x="670" y="1077" font-size="57">(800) 471-2965</text>
    <text class="cta-web" x="671" y="1116" font-size="22">www.bluegatehome.com</text>
    <text class="cta-license" x="671" y="1150" font-size="22">NMLS #318760</text>
  </g>
</svg>
</body>
</html>
```